Distribution/Printing company needs a web site to inform prospective customers on what we do.

Distribution/Printing/Packaging company needs a web site to inform prospective customers on what we do. Please look at our direct to consumer web site (under development) for an idea of the product lines we sell: storedev.kelbrynwares.com
Logo files are attached as is a flyer that is under development which contains other information about the company (this is to be used for content- not to be posted as is). The web site should be focused on our business customer base and is not intended to be direct to consumer. Site should have a link to our consumer web site.
Site design should be mobile friendly, or mobile could be redirected to a mobile version. This web site will be strictly informational and will not be designed for any sales transactions.

Manufacturing and retail businesses, any other multi-site business that would benefit from centralized pricing and budget controls we can provide (banks, medical/dental offices, educational facilities, etc).

• 1) Top level menu: Products, about us, locations, contact us, news
• 2) page with news/promotions that is easily updated
• 3) "contact us" form (name, company, phone, email address) email link
• 4) link to www.store.kelbrynwares.com with information that lower pricing is available for businesses
• 5) SEO keywords
• 6) Link to powerpoint presentation file
• 1) our phone number should appear on every page near the top

```html
<!DOCTYPE html>
<html lang="en">
<head>
<meta charset="utf-8">
<title>Kelbryn Wares — Packaging, Printing, Distribution</title>
<link rel="stylesheet" href="https://fonts.googleapis.com/css2?family=PT+Sans:ital,wght@0,400;0,700;1,400&family=Ubuntu:wght@300;400;500&display=swap">
<style>
:root{
  --navy:#0c3a68;
  --navy-deep:#06305a;
  --band-top:#2a6399;
  --band-bottom:#0a3765;
  --ink:#1b1b1b;
  --text:#555;
  --menu:#333333;
  --menu-line:#555;
  --sky:#e6eff7;
  --sky-mid:#d3e3f0;
  --tile:#c5d8e8;
  --field:#ffffff;
  --rule:#dde4ea;
}
*{box-sizing:border-box;margin:0;padding:0}
html,body{width:831px;height:1200px;overflow:hidden}
body{position:relative;background:#fff;font-family:"PT Sans",Arial,sans-serif;color:var(--ink)}
.abs{position:absolute}

/* header */
.topline{left:0;top:0;width:831px;height:4px;background:var(--navy-deep)}
.header{left:0;top:4px;width:831px;height:101px;background:#fff}
.brand{left:57px;top:50px;width:160px}
.brand-name{font:700 13px/1 "PT Sans",sans-serif;color:#1d1d1d;letter-spacing:.3px}
.brand-tag{font:700 8.5px/1 "PT Sans",sans-serif;color:#1d1d1d;margin-top:5px}
.lang-label{left:620px;top:20px;font:13px Arial,sans-serif;color:var(--navy)}
.lang-select{left:678px;top:16px;width:120px;height:23px;background:#e9eef3;border:1px solid #d6dde4;font:12px Arial,sans-serif;color:var(--navy);padding:4px 8px}
.lang-select .arrow{position:absolute;right:0;top:0;width:21px;height:21px;border-left:1px solid #c8d1da}
.nav a{position:absolute;top:72px;font:13px Arial,sans-serif;color:var(--navy);text-decoration:none}
.nav .active{left:372px;top:65px;width:61px;height:30px;background:var(--menu);color:#fff;padding:7px 0 0 4px}
.dropdown{left:372px;top:95px;width:150px;background:var(--menu)}
.dropdown li{list-style:none;height:28px;border-bottom:1px solid var(--menu-line);font:12px "PT Sans",sans-serif;color:#eee;padding:6px 0 0 9px}
.dropdown li:last-child{border-bottom:0}

/* hero */
.hero{left:0;top:105px;width:831px;height:320px;background:radial-gradient(ellipse at 30% 40%,#ffffff 0%,#edf3f9 45%,#d6e4f0 100%)}
.hero-photo{left:370px;top:105px;width:461px;height:320px;background:radial-gradient(ellipse at 48% 40%,#6b6763 0%,#3e3a38 22%,rgba(120,125,130,.55) 45%,rgba(214,228,240,0) 70%)}
.hero-title{left:110px;top:214px;font:700 15px/1 "PT Sans",sans-serif;color:var(--navy);letter-spacing:.3px}
.hero-tag{left:117px;top:233px;font:700 10px/1 "PT Sans",sans-serif;color:var(--navy)}
.hero-copy{left:60px;top:256px;width:310px;font:9.5px/1.6 "PT Sans",sans-serif;color:var(--navy)}
.btn{display:block;background:var(--navy);color:#fff;border-radius:14px;text-align:center;font:11.5px/27px "Ubuntu",sans-serif}
.hero-btn{left:57px;top:299px;width:79px;height:27px}
.dots{left:55px;top:392px;display:flex;gap:4px}
.dots span{width:10px;height:10px;border-radius:50%;background:#2a5f93}
.dots span:first-child{background:#000}

/* service band */
.band{left:15px;top:423px;width:804px;height:208px;border-radius:12px;background:linear-gradient(#2f6aa0,var(--band-bottom) 60%);overflow:hidden}
.band-divider{position:absolute;top:0;height:208px}
.service{position:absolute;top:0;width:240px;height:208px;color:#fff}
.service .photo{position:absolute;top:8px;width:184px;height:62px;border-radius:8px}
.service h2{position:absolute;top:71px;font:italic 400 24px/1 "PT Sans",sans-serif;display:flex;align-items:center;gap:6px}
.service h2 svg{width:20px;height:20px}
.service .sub{position:absolute;top:101px;font:12px "PT Sans",sans-serif}
.service .rule{position:absolute;top:119px;width:210px;height:1px;background:rgba(255,255,255,.25)}
.service p{position:absolute;top:125px;width:215px;font:italic 9.5px/1.7 "PT Sans",sans-serif}
.service .more{position:absolute;top:177px;font:12px "PT Sans",sans-serif}

/* content cards */
.card{position:absolute;top:653px;height:306px;background:#fff;border:1px solid var(--rule);border-radius:6px;box-shadow:0 4px 8px rgba(0,0,0,.06);padding:16px 14px}
.card h3{font:300 17.5px/1 "Ubuntu",sans-serif;color:var(--ink);margin-bottom:13px}
.welcome .lead{font:11px/1.45 "PT Sans",sans-serif;color:#111;text-align:justify;margin-bottom:10px}
.welcome p{font:9.5px/1.65 "PT Sans",sans-serif;color:var(--text);text-align:justify;margin-bottom:9px}
.offers .photo{width:229px;height:99px;border-radius:6px;background:radial-gradient(circle at 40% 95%,#5b86b8 0%,#8fb3d8 30%,#cfe0ef 65%,#e6eff7 100%);margin-bottom:10px}
.offers .lead{font:10.5px/1.5 "PT Sans",sans-serif;color:var(--navy);margin-bottom:6px}
.offers ul{list-style:none}
.offers li{height:19px;margin-bottom:3px;background:#eef3f7;font:10px/19px "PT Sans",sans-serif;color:var(--navy);padding-left:30px;position:relative}
.offers li::before{content:"";position:absolute;left:13px;top:7px;border-left:4px solid var(--navy);border-top:3px solid transparent;border-bottom:3px solid transparent}
.blog .post{font:italic 9.5px/1.55 "PT Sans",sans-serif;color:var(--navy);width:222px}
.blog .date{font:9.5px "PT Sans",sans-serif;color:#222;margin:5px 0 7px}
.blog .dotted{width:205px;border-top:1px dotted #999;margin-bottom:10px}

/* footer */
.footer{left:0;top:978px;width:831px;height:194px;background:linear-gradient(90deg,var(--sky-mid),var(--sky) 40%,#f1f6fa 60%,var(--sky-mid));border-top:1px solid #cad8e4}
.footer h4{position:absolute;font:400 18px/1 "Ubuntu",sans-serif;color:var(--navy)}
.field{position:absolute;left:30px;width:153px;background:var(--field);border-radius:6px;font:10.5px "PT Sans",sans-serif;color:#999;padding:4px 13px}
.social-icons{left:218px;top:1043px;display:flex;gap:7px}
.social-icons span{width:24px;height:24px;border-radius:50%;background:var(--navy)}
.social-links{left:218px;top:1087px;font:11px "PT Sans",sans-serif;color:var(--navy)}
.thumb{position:absolute;left:405px;width:50px;height:43px;border-radius:6px;background:var(--tile)}
.fpost{position:absolute;left:462px;width:140px;font:italic 9.5px/1.5 "PT Sans",sans-serif;color:var(--navy)}
.partner{position:absolute;width:49px;height:43px;border-radius:6px;background:var(--tile)}
.bottom-bar{left:0;top:1172px;width:831px;height:28px;background:#cbdbe8;font:10px/28px Arial,sans-serif;color:#1a2b3b;text-align:right;padding-right:46px}
</style>
</head>
<body>

<div class="abs topline"></div>
<header class="abs header"></header>
<div class="abs brand">
  <div class="brand-name">KELBRYN WARES</div>
  <div class="brand-tag">Packaging • Printing • Distribution</div>
</div>
<div class="abs lang-label">Language:</div>
<div class="abs lang-select">English<span class="arrow"><svg width="21" height="21" viewBox="0 0 21 21"><path d="M7 9h7l-3.5 4z" fill="#8a97a5"/></svg></span></div>

<nav class="nav">
  <a class="active">Packaging</a>
  <a style="left:457px">Office Supplies</a>
  <a style="left:562px">Janitorial</a>
  <a style="left:635px">Retail Supplies</a>
  <a style="left:740px">Contact US</a>
</nav>

<section class="abs hero"></section>
<div class="abs hero-photo" role="img" aria-label="Photo of a businessman in motion, blurred"></div>
<div class="abs hero-title">KELBRYN WARES</div>
<div class="abs hero-tag">Packaging • Printing • Distribution</div>
<p class="abs hero-copy">Pellentesque faucibus. Ut accumsan ultricies elit. Maecenas at justo id velit placerat molestie. Donec dictum lectus non odio.</p>
<a class="abs btn hero-btn">read more</a>
<div class="abs dots"><span></span><span></span><span></span><span></span></div>

<ul class="abs dropdown">
  <li>Bags - Poly</li><li>Kraft Paper</li><li>Bubble Wrap</li><li>Tape and Tape Dispensers</li>
  <li>Packing List Envelopes</li><li>Staples</li><li>Corrugated Boxes</li><li>Closures</li><li>Tissue</li>
</ul>

<section class="abs band">
  <svg class="band-divider" style="left:0" width="804" height="208">
    <path d="M306 0 L256 208" stroke="#fff" stroke-width="2.5" opacity=".85"/>
    <path d="M598 0 L550 208" stroke="#fff" stroke-width="2.5" opacity=".85"/>
  </svg>
  <div class="service" style="left:35px">
    <div class="photo" style="left:0;background:linear-gradient(135deg,#e9f2e6,#7fb36f 45%,#b48b5a)" role="img" aria-label="Photo of gift bags with green tissue"></div>
    <h2 style="left:7px"><svg viewBox="0 0 20 20"><path d="M4 16L14 6M7 5h8v8" stroke="#fff" stroke-width="3.5" fill="none"/></svg>Packaging</h2>
    <div class="sub" style="left:34px">Marketing tittle line goes here</div>
    <div class="rule" style="left:2px"></div>
    <p style="left:4px">Pellentesque faucibus. Ut accumsan ultricies elit. Maecenas at justo id velit placerat molestie. Donec dictum lectus non odio.</p>
    <div class="more" style="left:6px">learn more</div>
  </div>
  <div class="service" style="left:311px">
    <div class="photo" style="left:0;background:linear-gradient(90deg,#f3f3f3,#d9c6a4 50%,#b89466)" role="img" aria-label="Photo of printed cardboard boxes"></div>
    <h2 style="left:-2px"><svg viewBox="0 0 20 20"><rect x="1" y="1" width="14" height="18" fill="#fff"/><path d="M6 10h9M12 6l5 4-5 4" stroke="#0a3765" stroke-width="2.5" fill="none"/></svg>Printing</h2>
    <div class="sub" style="left:22px">Marketing tittle line goes here</div>
    <div class="rule" style="left:-10px"></div>
    <p style="left:-7px">Pellentesque faucibus. Ut accumsan ultricies elit. Maecenas at justo id velit placerat molestie. Donec dictum lectus non odio.</p>
    <div class="more" style="left:-6px">learn more</div>
  </div>
  <div class="service" style="left:587px">
    <div class="photo" style="left:0;background:linear-gradient(135deg,#e8e3e0,#d23a32 45%,#b8211d)" role="img" aria-label="Photo of a red shipping box"></div>
    <h2 style="left:0"><svg viewBox="0 0 20 20"><path d="M1 5h5l8 10h5M1 15h5l8-10h5" stroke="#fff" stroke-width="3" fill="none"/></svg>Distribution</h2>
    <div class="sub" style="left:24px">Marketing tittle line goes here</div>
    <div class="rule" style="left:-4px"></div>
    <p style="left:-3px">Pellentesque faucibus. Ut accumsan ultricies elit. Maecenas at justo id velit placerat molestie. Donec dictum lectus non odio.</p>
    <div class="more" style="left:-3px">learn more</div>
  </div>
</section>

<article class="card welcome" style="left:22px;width:256px">
  <h3>Welcome to Our Site !</h3>
  <p class="lead">Pellentesque faucibus. Ut accumsan ultricies elit. Maecenas at justo id velit placerat molestie.</p>
  <p>Cras a ante vitae enim iaculis aliquam. Mauris nunc quam, venenatis nec, euismod sit amet, egestas placerat, est. Pellentesque habitant morbi tristique senectus et netus et malesuada fames ac turpis egestas. Cras id elit. Integer quis urna. Ut ante enim, dapibus malesuada, fringilla eu, condimentum quis, tellus.</p>
  <p>Aenean porttitor eros vel dolor. Donec convallis pede venenatis nibh. Duis quam. Nam eget lacus. Aliquam erat volutpat. Quisque dignissim congue leo. Donec scelerisque leo ac risus. Praesent sit amet est. In dictum, dolor eu dictum porttitor.</p>
</article>

<article class="card offers" style="left:291px;width:257px">
  <h3>Offers &amp; Services Provided</h3>
  <div class="photo" role="img" aria-label="Illustration of people connected around a globe"></div>
  <p class="lead">Pellentesque faucibus. Ut accumsan ultricies elit. Maecenas at justo id</p>
  <ul>
    <li>Lorem ipsum dolor sit amet</li>
    <li>Consectetuer adipiscing elit.</li>
    <li>Nam cursus Morbi ut mi Nullam</li>
    <li>Condimentum at laoreet mattis massa.</li>
    <li>Ed eleifend nonummy diam.</li>
  </ul>
</article>

<article class="card blog" style="left:559px;width:257px">
  <h3>Recent Blog</h3>
  <p class="post">Pellentesque faucibus. Ut accumsan ultricies elit. Maecenas at justo id velit placerat molestie.</p>
  <p class="date">Posted on 20.12.2012</p>
  <div class="dotted"></div>
  <p class="post">Lorem ipsum dolor sit amet, consectetuer adipiscing elit. Nam cursus. Morbi ut mi. Nullam enim leo, egestas id, condimentum at, laoreet mattis, massa. Sed eleifend nonummy diam.</p>
  <p class="date">Posted on 20.12.2012</p>
  <div class="dotted"></div>
  <p class="post">Lorem ipsum dolor sit amet, consectetuer adipiscing elit. Nam cursus. Morbi ut mi. Nullam enim leo, egestas id, condimentum at, laoreet mattis, massa. Sed eleifend nonummy diam.</p>
  <p class="date">Posted on 20.12.2012</p>
</article>

<footer class="abs footer">
  <h4 style="left:34px;top:14px">Contact</h4>
  <div class="field" style="top:49px;height:21px">Name</div>
  <div class="field" style="top:76px;height:21px">Email</div>
  <div class="field" style="top:104px;height:38px">Message</div>
  <a class="abs btn" style="left:68px;top:154px;width:79px;height:26px;line-height:26px;font-size:14px">send</a>

  <h4 style="left:222px;top:17px">Social media</h4>
  <h4 style="left:411px;top:17px">Blog</h4>
  <div class="thumb" style="top:63px"></div>
  <p class="fpost" style="top:63px">Lorem ipsum dolor sit amet, consectetuer adipiscing elit. Nam cursus.</p>
  <div class="thumb" style="top:120px"></div>
  <p class="fpost" style="top:118px">Lorem ipsum dolor sit amet, consectetuer adipiscing elit. Nam cursus.</p>

  <h4 style="left:610px;top:14px">Partners</h4>
  <div class="partner" style="left:610px;top:59px"></div>
  <div class="partner" style="left:673px;top:59px"></div>
  <div class="partner" style="left:737px;top:59px"></div>
  <div class="partner" style="left:610px;top:114px"></div>
  <div class="partner" style="left:673px;top:114px"></div>
  <div class="partner" style="left:737px;top:114px"></div>
</footer>
<div class="abs social-icons"><span></span><span></span><span></span><span></span></div>
<div class="abs social-links">Friendbook | LinkUp | Chirper | Feedline</div>

<div class="abs bottom-bar">All Right Reserved 2015. Kelbryn Wares.</div>

</body>
</html>
```